I need a website designed for my hair extensions business

I have some before and afters you can use

https://example-photos.test/p/Qm4rzaLwTbN/

https://www.example-photos.test/p/Kvpuw7HTeGL/?ref=QjZkNTRmYzEwYWE==
Hi I offer tiny weave hair extensions
My instagram page is Verandahairextensionsgeelong

I’m needing a Lux website
I have been doing weave hair extensions for 16 years and I specialise in only the finest installation and hair quality

The website must attract a high profile cliental

I have thousands of photos on my instagram page you can use

The website must be coded to attract hair extensions clients from all over Victoria Australia
It must have what’s relevant for google to recognise the website to Potential clients

recognise

Some are the below
Apologies for the confusion. Here are some SEO keywords that can be used for a website focused on Weave Hair Extensions in Victoria, Australia:

1. Weave hair extensions Victoria
2. Best weave hair extensions Australia
3. Affordable weave hair extensions
4. Professional weave hair extensions
5. High-quality weave hair extensions
6. Victoria weave hair extension services
7. Top-rated weave hair extension salon
8. Natural-looking weave hair extensions
9. Customizable weave hair extensions
10. Victoria's premier weave hair extensions

Remember to incorporate these keywords strategically into your website's content, including titles, headings, meta descriptions, and throughout the body text. This will help improve your website's visibility in search engine results and attract relevant traffic from individuals looking for weave hair extensions in Victoria, Australia.

Please make the website look elegant not tacky no pink or script writing please

Target Market(s)

Woman between 21 to 60

Industry/Entity Type

https://www.example-photos.test/reel/BtwwkLPHn7M/?ref=QjZkNTRmYzEwYWE==

Coding

Coded - Design and coding required

Number of Pages Required

3 page

Requirements
Must have
• Description of myself 16 years experience, I’ve installed 1000s of weave hair extensions, my intention to deal is guaranteed.
Nice to have
• I have added 2 images or how flat and tiny the weave hair extensions are, here is a link to a video that can be used https://www.example-photos.test/reel/BtwwkLPHn7M/?ref=QjZkNTRmYzEwYWE== The website should look elegant, the extensions I install are spectacular. You can see the before and after on my instagram page veranda hair extensions Geelong. The pictures of my work should be taken from my instagram page as I own those photos
Should not have
• My website should not have pink or script writing it needs to attract a high cliental the website must look elegant

```html
<!DOCTYPE html>
<html lang="en">
<head>
<meta charset="utf-8">
<title>Veranda Hair Extensions — Weave Hair Extensions Victoria</title>
<link href="https://fonts.googleapis.com/css2?family=Fraunces:opsz,wght@9..144,400;9..144,500&family=Mulish:wght@400;600;700&display=swap" rel="stylesheet">
<style>
:root{
  --ink:#1f1a17;
  --muted:#7b716b;
  --tan:#d2aa8c;
  --tan-dark:#c39376;
  --accent:#c98f6a;
  --ivory:#fbf8f3;
  --white:#ffffff;
  --track:#e8ddd3;
  --quote:#efe1d4;
}
*{margin:0;padding:0;box-sizing:border-box}
html,body{width:1200px;height:4827px;overflow:hidden}
body{position:relative;background:var(--ivory);font-family:'Mulish',sans-serif;color:var(--ink)}
.abs{position:absolute}
.serif{font-family:'Fraunces',serif;font-weight:400}
.eyebrow{font-size:9px;letter-spacing:1.5px;text-transform:uppercase;color:var(--accent);font-weight:700}
.center{text-align:center;left:0;width:1200px}
.photo{position:absolute}
.btn{position:absolute;background:var(--tan);color:#fff;font-size:9px;letter-spacing:1.5px;text-transform:uppercase;font-weight:700;display:flex;align-items:center;justify-content:center}

/* header + hero */
.hero{position:absolute;left:0;top:0;width:1200px;height:543px;background:linear-gradient(90deg,#f8f1dc 0%,#f6ecdf 45%,#f1e4d6 75%,#eedfd0 100%)}
.logo{left:213px;top:12px;font-family:'Fraunces',serif;font-size:28px;color:var(--tan-dark);letter-spacing:1px}
.nav{left:418px;top:22px;display:flex;gap:34px;font-size:9.5px;font-weight:700;letter-spacing:1px;text-transform:uppercase}
.hero-title{left:208px;top:128px;font-size:48px;line-height:51px}
.hero-text{left:208px;top:348px;width:280px;font-size:11px;line-height:18px;color:var(--muted)}
.quote-text{left:810px;top:282px;width:180px;font-size:11px;line-height:17px;color:var(--muted)}
.quote-name{left:810px;top:348px;font-size:13px;display:flex;align-items:center;gap:12px}
.quote-name::after{content:"";width:38px;height:1px;background:var(--ink)}

/* why */
.why-item{position:absolute;top:768px;width:260px;text-align:center}
.why-item h3{font-family:'Fraunces',serif;font-weight:400;font-size:18px;margin-top:28px}
.why-item p{font-size:10.5px;line-height:17px;color:var(--muted);margin-top:6px}

/* skills */
.skill{position:absolute;left:623px;width:339px}
.skill .row{display:flex;justify-content:space-between;font-family:'Fraunces',serif;font-size:13.5px}
.skill .track{margin-top:10px;height:4px;background:var(--track)}
.skill .fill{height:4px;background:var(--tan)}

/* services */
.services-band{position:absolute;left:0;top:1993px;width:1200px;height:648px;background:var(--tan)}
.card-cap{position:absolute;width:230px;height:120px;background:var(--tan);padding:26px 12px 0}
.card-cap h3{font-family:'Fraunces',serif;font-weight:400;font-size:19px;color:#fff}
.card-cap p{font-size:10px;line-height:16px;color:#efdccf;margin-top:8px}
.card-cap span{display:block;margin-top:12px;font-size:8px;font-weight:700;letter-spacing:1.2px;color:#fff}
.stats{position:absolute;left:208px;top:2585px;width:784px;height:115px;background:#fff;display:flex;box-shadow:0 4px 14px rgba(0,0,0,.05)}
.stat{flex:1;text-align:center;padding-top:30px;border-right:1px solid #eee6dd}
.stat:last-child{border-right:0}
.stat b{display:block;font-family:'Fraunces',serif;font-weight:400;font-size:26px}
.stat small{display:block;margin-top:8px;font-size:8.5px;letter-spacing:1.2px;font-weight:700;color:var(--accent);text-transform:uppercase}

/* price */
.price{position:absolute;left:208px;width:277px;display:flex;justify-content:space-between;font-size:13px}
.price .name{font-family:'Fraunces',serif}
.price .amt{font-family:'Fraunces',serif;color:var(--accent)}
.hours{left:538px;top:2992px;width:202px;height:223px;background:#fff;text-align:center;box-shadow:0 6px 20px rgba(0,0,0,.06)}
.hours h4{font-family:'Fraunces',serif;font-weight:400;font-size:19px;margin-top:28px}
.hours .lbl{font-size:8.5px;font-weight:700;letter-spacing:1px;margin-top:30px}
.hours .val{font-size:11px;color:var(--muted);margin-top:6px}

/* reviews */
.review{position:absolute;top:3455px;width:320px;text-align:center;font-size:12px;line-height:19px}
.review .mark{position:absolute;left:50%;top:-22px;transform:translateX(-50%);font-family:'Fraunces',serif;font-size:100px;line-height:1;color:var(--quote);z-index:0}
.review p{position:relative;z-index:1}
.reviewer{position:absolute;top:3525px;display:flex;align-items:center;gap:10px}
.avatar{width:38px;height:38px;border-radius:50%;background:#a8968a}
.reviewer b{display:block;font-family:'Fraunces',serif;font-weight:400;font-size:14px;color:var(--accent)}
.reviewer small{font-size:10px;color:var(--muted)}

/* newsletter */
.news{position:absolute;left:214px;top:4537px;width:772px;height:156px;background:var(--tan)}
.news h3{position:absolute;left:32px;top:30px;font-family:'Fraunces',serif;font-weight:400;font-size:24px;color:#fff}
.news p{position:absolute;left:32px;top:76px;width:380px;font-size:10.5px;line-height:17px;color:#f4e3d7}
.news .field{position:absolute;left:470px;top:56px;width:140px;padding-bottom:6px;border-bottom:1px solid #e9d2c2;font-size:10px;color:#f1dccd}
.news .sub{position:absolute;left:626px;top:50px;width:102px;height:40px;background:#fff;color:var(--accent);font-size:8.5px;font-weight:700;letter-spacing:1.2px;display:flex;align-items:center;justify-content:center}

.footer{position:absolute;left:0;top:4760px;width:1200px;height:67px;background:#f3eee7;font-size:9.5px;color:var(--muted)}
</style>
</head>
<body>

<section class="hero">
  <div class="abs logo">VERANDA</div>
  <nav class="abs nav"><span>Home ▾</span><span>About</span><span>Services ▾</span><span>Pages ▾</span><span>Contact us</span></nav>
  <div class="btn" style="left:898px;top:12px;width:92px;height:32px">Price list</div>
  <h1 class="abs serif hero-title">We Offer<br>Tiny Weave<br>Hair<br>Extensions</h1>
  <p class="abs hero-text">Lorem ipsum dolor sit amet, consetetur sadipscing elitr, sed diam nonumy eirmod tempor.</p>
  <div class="btn" style="left:208px;top:413px;width:160px;height:36px">Book appointment</div>
  <div class="photo" role="img" aria-label="Woman with long wavy brown hair extensions" style="left:535px;top:160px;width:245px;height:383px;background:linear-gradient(180deg,#a07a5e 0%,#7a5640 55%,#e9e2dc 100%)"></div>
  <div class="abs serif" style="left:808px;top:232px;font-size:46px;color:var(--accent);line-height:1">“</div>
  <p class="abs quote-text">"It really saves me time and effort. Hair Extension is exactly what I want. It's just amazing."</p>
  <div class="abs serif quote-name">Clara Whitfield</div>
</section>

<div class="abs eyebrow center" style="top:651px">Our standard qualities</div>
<h2 class="abs serif center" style="top:672px;font-size:34px">Why Choose Us?</h2>

<div class="why-item" style="left:208px">
  <svg width="64" height="56" viewBox="0 0 64 56" fill="none" stroke="#b27a5a" stroke-width="1.6"><circle cx="38" cy="24" r="20"/><rect x="10" y="18" width="10" height="34"/><line x1="24" y1="12" x2="24" y2="52"/><line x1="30" y1="22" x2="30" y2="52"/><line x1="4" y1="52" x2="60" y2="52"/></svg>
  <h3>16 Years of Experience</h3>
  <p>Lorem ipsum dolor sit amet, consectetur<br>adipiscing elit. Ut elit tellus.</p>
</div>
<div class="why-item" style="left:470px">
  <svg width="70" height="56" viewBox="0 0 70 56" fill="none" stroke="#b27a5a" stroke-width="1.6"><circle cx="20" cy="18" r="9"/><circle cx="50" cy="18" r="9"/><circle cx="35" cy="28" r="10"/><path d="M4 48c0-10 8-16 16-16M66 48c0-10-8-16-16-16M18 54c0-10 8-14 17-14s17 4 17 14"/></svg>
  <h3>We're Professional</h3>
  <p>Lorem ipsum dolor sit amet, consectetur<br>adipiscing elit. Ut elit tellus.</p>
</div>
<div class="why-item" style="left:732px">
  <svg width="50" height="56" viewBox="0 0 50 56" fill="none" stroke="#b27a5a" stroke-width="1.6"><rect x="6" y="4" width="38" height="48"/><line x1="14" y1="14" x2="36" y2="14"/><line x1="14" y1="20" x2="36" y2="20"/><circle cx="25" cy="34" r="7"/><path d="M21 40l-2 10 6-4 6 4-2-10"/></svg>
  <h3>Certified Hair Technician</h3>
  <p>Lorem ipsum dolor sit amet, consectetur<br>adipiscing elit. Ut elit tellus.</p>
</div>

<div class="photo" role="img" aria-label="Video still: stylist curling a client's hair in the salon" style="left:208px;top:992px;width:784px;height:353px;background:linear-gradient(90deg,#8a6a54 0%,#c8b3a4 45%,#aeaaa8 75%,#9a8a80 100%)"></div>
<svg class="abs" style="left:577px;top:1146px" width="46" height="46" viewBox="0 0 46 46"><circle cx="23" cy="23" r="22" fill="#fff" opacity=".9"/><path d="M18 14l14 9-14 9z" fill="#8a6a54"/></svg>

<div class="photo" role="img" aria-label="Stylist in mask and gloves working on a client's curly hair" style="left:214px;top:1532px;width:347px;height:345px;background:linear-gradient(135deg,#5d7a52 0%,#c8b7a6 50%,#e9e4df 100%)"></div>
<div class="abs eyebrow" style="left:623px;top:1560px">Know more</div>
<h2 class="abs serif" style="left:623px;top:1578px;font-size:34px">Our team skills</h2>
<div class="skill" style="top:1658px"><div class="row"><span>Hairdressing</span><span>97%</span></div><div class="track"><div class="fill" style="width:97%"></div></div></div>
<div class="skill" style="top:1717px"><div class="row"><span>Assist Stylist</span><span>93%</span></div><div class="track"><div class="fill" style="width:93%"></div></div></div>
<div class="skill" style="top:1776px"><div class="row"><span>Salon Environment</span><span>82%</span></div><div class="track"><div class="fill" style="width:82%"></div></div></div>
<div class="skill" style="top:1835px"><div class="row"><span>Drive and Energy</span><span>90%</span></div><div class="track"><div class="fill" style="width:90%"></div></div></div>

<section class="services-band">
  <div class="abs eyebrow center" style="top:62px;color:#fff">Our services</div>
  <h2 class="abs serif center" style="top:80px;font-size:34px;color:#fff">Service Beyond Expectation</h2>
</section>
<div class="photo" role="img" aria-label="Portrait of a woman with sleek brown hair" style="left:208px;top:2155px;width:250px;height:275px;background:linear-gradient(180deg,#e7e3e1 0%,#b8a193 100%)"></div>
<div class="photo" role="img" aria-label="Portrait of a woman with dark voluminous curls" style="left:475px;top:2155px;width:250px;height:275px;background:linear-gradient(180deg,#9a8f8b 0%,#4a3a34 100%)"></div>
<div class="photo" role="img" aria-label="Portrait of a woman with vivid coloured hair" style="left:742px;top:2155px;width:250px;height:275px;background:linear-gradient(180deg,#b9a6ad 0%,#8f5a7e 100%)"></div>
<div class="card-cap" style="left:208px;top:2375px"><h3>Service 1</h3><p>Lorem ipsum dolor sit amet,<br>consectetur adipiscing elit, sed do</p><span>VIEW SERVICE →</span></div>
<div class="card-cap" style="left:475px;top:2375px"><h3>Service 2</h3><p>Lorem ipsum dolor sit amet,<br>consectetur adipiscing elit, sed do</p><span>VIEW SERVICE →</span></div>
<div class="card-cap" style="left:742px;top:2375px"><h3>Service 3</h3><p>Lorem ipsum dolor sit amet,<br>consectetur adipiscing elit, sed do</p><span>VIEW SERVICE →</span></div>

<div class="stats">
  <div class="stat"><b>16+</b><small>Years of experience</small></div>
  <div class="stat"><b>5</b><small>Hair technician</small></div>
  <div class="stat"><b>1000+</b><small>Services completed</small></div>
  <div class="stat"><b>1000+</b><small>Happy customers</small></div>
</div>

<div class="abs eyebrow" style="left:208px;top:2784px">Pricing</div>
<h2 class="abs serif" style="left:208px;top:2803px;font-size:34px">Price List</h2>
<div class="price" style="top:2872px"><span class="name">Blow Dry</span><span class="amt">From $25</span></div>
<div class="price" style="top:2930px"><span class="name">Basic Tint</span><span class="amt">From $45</span></div>
<div class="price" style="top:2988px"><span class="name">Organic Color</span><span class="amt">From $50</span></div>
<div class="price" style="top:3046px"><span class="name">Full Highlights</span><span class="amt">From $70</span></div>
<div class="btn" style="left:208px;top:3105px;width:119px;height:36px">View all →</div>
<div class="photo" role="img" aria-label="Stylist applying colour to sectioned long hair" style="left:623px;top:2780px;width:367px;height:360px;background:linear-gradient(135deg,#d7d2cf 0%,#8a6750 50%,#e3d9d2 100%)"></div>
<div class="abs hours">
  <h4>Open Hours</h4>
  <div class="lbl">MONDAY - SATURDAY</div>
  <div class="val">08.00 - 15.00</div>
  <div class="lbl">SUNDAYS</div>
  <div class="val">Closed</div>
</div>

<div class="abs eyebrow center" style="top:3332px">Reviews</div>
<h2 class="abs serif center" style="top:3350px;font-size:32px">What our customers say</h2>
<div class="review" style="left:250px"><span class="mark">“</span><p>"I could probably go into sales for you. Definitely worth the investment. We've used hair salon for the last five years."</p></div>
<div class="review" style="left:630px"><span class="mark">“</span><p>"Absolutely wonderful! We can't understand how we've been living without hair salon. I am completely blown away."</p></div>
<div class="reviewer" style="left:333px"><div class="avatar" role="img" aria-label="Customer photo"></div><div><b>Mira Lennox</b><small>Customer</small></div></div>
<div class="reviewer" style="left:725px"><div class="avatar" role="img" aria-label="Customer photo"></div><div><b>Tessa Rowan</b><small>Customer</small></div></div>

<div class="abs" style="left:0;top:3655px;width:1200px;height:1105px;background:#fff"></div>
<div class="abs eyebrow center" style="top:3738px">Galleries</div>
<h2 class="abs serif center" style="top:3756px;font-size:34px">Salon gallery</h2>
<div class="photo" role="img" aria-label="Stylist blow-drying a client's hair" style="left:222px;top:3912px;width:243px;height:275px;background:linear-gradient(135deg,#e8e6e4 0%,#3a302c 70%)"></div>
<div class="photo" role="img" aria-label="Woman with long straight brown hair extensions" style="left:222px;top:4200px;width:243px;height:220px;background:linear-gradient(180deg,#ebe3de 0%,#8d6148 100%)"></div>
<div class="photo" role="img" aria-label="Stylist presenting long straight hair on a client" style="left:479px;top:3840px;width:242px;height:345px;background:linear-gradient(180deg,#3d3633 0%,#9b6c4c 60%,#2a2523 100%)"></div>
<div class="photo" role="img" aria-label="Bright modern salon interior" style="left:479px;top:4198px;width:242px;height:212px;background:linear-gradient(180deg,#e4e4e2 0%,#b7b5b2 60%,#3a3a3a 100%)"></div>
<div class="photo" role="img" aria-label="Back view of long blonde curls" style="left:735px;top:3877px;width:243px;height:241px;background:linear-gradient(180deg,#d6d4d3 0%,#c49a6c 60%,#b98d62 100%)"></div>
<div class="photo" role="img" aria-label="Stylist drying a client's hair with a hairdryer" style="left:735px;top:4132px;width:243px;height:303px;background:linear-gradient(135deg,#2e2a29 0%,#9c6a4f 55%,#d9c5b8 100%)"></div>

<section class="news">
  <h3>Subscribes to Our Newsletter</h3>
  <p>Lorem ipsum dolor sit amet, consectetur adipiscing elit. Ut elit tellus, luctus nec ullamcorper mattis, pulvinar dapibu.</p>
  <div class="field">Your email</div>
  <div class="sub">SUBSCRIBE</div>
</section>

<footer class="footer">
  <span class="abs" style="left:222px;top:27px">© 2023, Web Design by Northgate Studio</span>
  <span class="abs" style="left:834px;top:27px">Help &amp; Support</span>
  <span class="abs" style="left:915px;top:27px">Privacy Policy</span>
</footer>

</body>
</html>
```